Flyers

Modify Existing Flyer and create another for exterior company
Updates

Previous Brief has been updated- we want to update this existing one also

Target Market(s)

Exterior Remodeling Customers

Industry/Entity Type

Remodeling/Construction

```html
<!DOCTYPE html>
<html lang="en">
<head>
<meta charset="utf-8">
<title>Northvale Roofing and Exteriors – Exterior Remodeling Flyer</title>
<link href="https://fonts.googleapis.com/css2?family=Open+Sans:wght@400;600;700;800&display=swap" rel="stylesheet">
<style>
:root{
  --charcoal:#333232;
  --stone:#c9c6c0;
  --ink:#2f2f2f;
  --icon:#4a4948;
  --white:#ffffff;
  --brand-orange:#e8562a;
  --frame:#2b2b2b;
  --overlay:rgba(51,50,50,.72);
}
*{margin:0;padding:0;box-sizing:border-box}
html,body{width:845px;height:1200px;overflow:hidden;background:var(--charcoal)}
body{font-family:"Open Sans",sans-serif;color:var(--ink)}
.flyer{position:relative;width:845px;height:1200px;background:var(--charcoal);overflow:hidden}

/* header */
.brand{position:absolute;left:24px;top:44px;display:flex;align-items:center;gap:8px}
.brand-mark{width:14px;height:14px;background:var(--brand-orange)}
.brand-name{font-weight:700;font-size:17px;color:var(--brand-orange);letter-spacing:.2px;line-height:1.15}
.cta{position:absolute;right:20px;top:22px;text-align:center;color:var(--white);width:240px}
.cta-line{font-size:20px;line-height:24px;font-weight:400}
.cta-line strong{font-weight:700}
.cta-phone{display:flex;align-items:center;justify-content:center;gap:14px;margin-top:10px;font-size:26px}
.cta-phone svg{width:40px;height:40px}

/* hero */
.hero-photo{position:absolute;top:146px;height:515px}
.hero-left{left:0;width:276px;background:linear-gradient(180deg,#cfd8de 0%,#aebbc4 30%,#5b5f63 48%,#6e6a64 72%,#3a3836 100%)}
.hero-right{left:292px;width:553px;background:linear-gradient(165deg,#dfe6ea 0%,#c9d2d6 35%,#8e969a 58%,#7c8a6c 78%,#5f6b4f 100%);clip-path:polygon(0 0,290px 0,553px 22px,553px 100%,0 100%)}
.hero-question{position:absolute;left:55px;top:446px;width:443px;height:107px;background:var(--overlay);color:var(--white);padding:2px 0 0 16px;font-size:29px;line-height:34px;font-weight:400}
.hero-question strong{font-weight:700}
.hero-headline{position:absolute;left:56px;top:588px;color:var(--white);font-weight:800;font-size:30.5px;line-height:28px;text-shadow:0 2px 4px rgba(0,0,0,.45)}

/* services */
.services{position:absolute;left:0;top:693px;width:845px;height:477px;background:var(--stone)}
.service-photo{position:absolute;width:156px;height:155px;border:4px solid var(--frame)}
.service-icon{position:absolute;width:34px;height:30px}
.service-title{position:absolute;font-weight:700;font-size:13.5px;letter-spacing:.3px;color:var(--ink);white-space:nowrap}
.service-copy{position:absolute;font-size:11px;line-height:16px;color:var(--ink)}
.service-copy ul{margin-top:10px;padding-left:16px}
.service-copy li{line-height:16.2px}

.footer{position:absolute;left:0;top:1170px;width:845px;height:30px;text-align:center;color:var(--white);font-size:13px;line-height:30px}
</style>
</head>
<body>
<div class="flyer">

  <header>
    <div class="brand">
      <span class="brand-mark"></span>
      <span class="brand-name">NORTHVALE<br>ROOFING AND EXTERIORS</span>
    </div>
    <div class="cta">
      <p class="cta-line">CALL TODAY FOR YOUR</p>
      <p class="cta-line"><strong>FREE</strong> ESTIMATE</p>
      <p class="cta-phone">
        <svg viewBox="0 0 40 40" aria-hidden="true"><circle cx="20" cy="20" r="20" fill="#fff"/><path d="M14 11c1-.6 2-.4 2.6.5l2 3c.5.8.3 1.8-.4 2.3l-1.3 1c.9 2 2.3 3.5 4.3 4.4l1-1.3c.6-.7 1.6-.9 2.3-.4l3 2c.9.6 1.1 1.7.5 2.6l-1.2 1.6c-.8 1-2.2 1.4-3.5.9-5-1.9-8.9-5.8-10.8-10.8-.5-1.3-.1-2.7.9-3.5z" fill="#333232"/></svg>
        555-014-2870
      </p>
    </div>
  </header>

  <section class="hero">
    <div class="hero-photo hero-left" role="img" aria-label="Close view of a new shingle roof line under a clear sky"></div>
    <div class="hero-photo hero-right" role="img" aria-label="Two-story house with fresh siding, new windows and a green front lawn"></div>
    <h1 class="hero-question">Ready for<br>a Durable and Beautiful<br><strong>Roof</strong> or <strong>Exterior</strong>?</h1>
    <h2 class="hero-headline">WORK&nbsp; WITH A TOP-RATED LOCAL EXTERIOR<br>REMODELING COMPANY IN ANKENY, IA</h2>
  </section>

  <section class="services">
    <!-- roofing -->
    <div class="service-photo" style="left:6px;top:64px;background:linear-gradient(180deg,#bcc8d0 0%,#9aa6ae 35%,#4e4f52 60%,#6d645b 100%)" role="img" aria-label="Crew installing asphalt shingles on a roof"></div>
    <svg class="service-icon" style="left:177px;top:12px" viewBox="0 0 34 30" role="img" aria-label="Roof icon"><path d="M2 16 17 3l15 13M7 12v15h20V12M14 27v-8h6v8" fill="none" stroke="var(--icon)" stroke-width="1.6" stroke-linejoin="round"/></svg>
    <h3 class="service-title" style="left:219px;top:30px">ROOFING</h3>
    <div class="service-copy" style="left:178px;top:55px;width:262px">
      <p>Whatever the weather brings to your home, our crew will keep your roof strong and dry.<br>You can trust us for:</p>
      <ul>
        <li>Roof replacement services</li>
        <li>Roof repair services</li>
        <li>Storm and hail damage repair</li>
        <li>Insurance claim assistance</li>
        <li>Shingle and metal roofing</li>
        <li>Flashing and vent upgrades</li>
        <li>Roof inspection services</li>
        <li>Skylight installation services</li>
        <li>Attic ventilation services</li>
      </ul>
    </div>

    <!-- siding -->
    <div class="service-photo" style="left:452px;top:64px;background:linear-gradient(180deg,#d6dde0 0%,#b7c2c8 40%,#8f9aa0 75%,#7a8a64 100%)" role="img" aria-label="House wall with new horizontal lap siding"></div>
    <svg class="service-icon" style="left:616px;top:12px" viewBox="0 0 34 30" role="img" aria-label="Siding icon"><rect x="3" y="3" width="28" height="24" fill="none" stroke="var(--icon)" stroke-width="1.6"/><path d="M3 9h28M3 15h28M3 21h28" stroke="var(--icon)" stroke-width="1.4"/></svg>
    <h3 class="service-title" style="left:660px;top:30px">SIDING</h3>
    <div class="service-copy" style="left:616px;top:55px;width:225px">
      <p>No matter what look you want for your home, our team will bring your vision to life.<br>You can hire us for:</p>
      <ul style="padding-left:22px">
        <li>Vinyl siding installation</li>
        <li>Fiber cement siding</li>
        <li>Engineered wood siding</li>
        <li>Siding repair services</li>
        <li>Soffit and fascia</li>
        <li>Seamless gutters</li>
        <li>Exterior trim and wraps</li>
      </ul>
    </div>

    <!-- windows & doors -->
    <div class="service-photo" style="left:7px;top:310px;background:linear-gradient(135deg,#e3e6e4 0%,#b9c3c8 40%,#8a94a0 65%,#5a5450 100%)" role="img" aria-label="New front entry door and double-hung windows"></div>
    <svg class="service-icon" style="left:177px;top:264px" viewBox="0 0 34 30" role="img" aria-label="Window icon"><rect x="5" y="2" width="24" height="26" fill="none" stroke="var(--icon)" stroke-width="1.6"/><path d="M17 2v26M5 15h24" stroke="var(--icon)" stroke-width="1.4"/></svg>
    <h3 class="service-title" style="left:220px;top:280px">WINDOWS &amp; DOORS</h3>
    <div class="service-copy" style="left:182px;top:305px;width:265px">
      <p>When you hire us to replace your windows and doors, the benefits are endless.<br>Our experienced and talented team can:</p>
      <ul>
        <li>Install energy-efficient windows</li>
        <li>Replace your front entry door</li>
        <li>Install patio and sliding doors</li>
        <li>Upgrade your garage door</li>
        <li>Seal drafts and lower energy bills</li>
      </ul>
    </div>

    <!-- decks/patios -->
    <div class="service-photo" style="left:452px;top:310px;background:linear-gradient(180deg,#b36a3f 0%,#6f8a4a 35%,#4f7a3a 55%,#8c7a70 80%,#6e6059 100%)" role="img" aria-label="Wooden deck with pergola and patio furniture"></div>
    <svg class="service-icon" style="left:616px;top:264px" viewBox="0 0 34 30" role="img" aria-label="Patio umbrella icon"><path d="M4 12Q17 0 30 12Z" fill="none" stroke="var(--icon)" stroke-width="1.6" stroke-linejoin="round"/><path d="M17 12v15M9 27h16" stroke="var(--icon)" stroke-width="1.6"/></svg>
    <h3 class="service-title" style="left:659px;top:280px">DECKS/PATIOS</h3>
    <div class="service-copy" style="left:625px;top:305px;width:216px">
      <p>An outdoor space is a great addition to any residential property. When you decide to build a patio or deck, you'll be able to enjoy a variety of benefits. Your outdoor area will increase your:</p>
      <ul style="padding-left:20px">
        <li>Property value</li>
        <li>Curb appeal</li>
        <li>Functional living space</li>
      </ul>
    </div>
  </section>

  <footer class="footer">www.northvaleexteriors.com</footer>
</div>
</body>
</html>
```